Corvid Lens Studio Business Card Design

I need a business card designed for a photography business based in Perth, Western Australia called Corvid Lens Studio.

We specialise in wedding, event photography and portrait photography.

The business card must borrow the style of the attached logo.

The hex codes for the colours in the logo are:
#ED1D85 - Pink
#89C23E - Green
#37282F - Black

The name on the card will be:
Name: Tobiah
Phone: 0417395268
Website: www.corvidlensstudio.com.au
Facebook: corvidlensstudio

I am open and happy to accept creative concepts.

Industry/Entity Type

Business

```html
<!DOCTYPE html>
<html lang="en">
<head>
<meta charset="utf-8">
<title>Corvid Lens Studio — Business Card</title>
<link rel="stylesheet" href="https://fonts.googleapis.com/css2?family=Cinzel:wght@700&family=Montserrat:wght@400&family=Open+Sans:wght@400&display=swap">
<style>
  :root {
    --pink: #ED1D85;
    --green: #89C23E;
    --ink: #37282F;
    --card-dark: #42353b;
    --paper: #ffffff;
    --backdrop: #ebe6de;
    --soft-white: #f4f0f2;
  }
  * { margin: 0; padding: 0; box-sizing: border-box; }
  html, body {
    width: 1196px; height: 1200px; overflow: hidden;
    background: var(--backdrop);
  }
  .canvas { position: relative; width: 1196px; height: 1200px; }

  .card {
    position: absolute;
    width: 854px; height: 485px;
    border-radius: 26px;
    overflow: hidden;
    box-shadow: 0 4px 14px rgba(0,0,0,0.18);
  }
  .card--front { left: 168px; top: 86px; background: var(--paper); }
  .card--back  { left: 190px; top: 620px; background: var(--card-dark); }

  .card__shapes { position: absolute; inset: 0; width: 100%; height: 100%; }

  .brand-mark {
    position: absolute; left: 228px; top: 34px;
    width: 124px; height: 124px;
    border: 2px solid var(--pink); border-radius: 50%;
    display: flex; align-items: center; justify-content: center;
  }
  .brand-mark__name {
    font-family: "Montserrat", sans-serif; font-size: 11px;
    letter-spacing: 0.08em; color: var(--ink);
    text-transform: uppercase; text-align: center; line-height: 1.5;
  }

  .wordmark {
    position: absolute; left: 38px; top: 190px;
    font-family: "Montserrat", sans-serif; font-weight: 400;
    font-size: 17px; letter-spacing: 0.44em;
    color: var(--ink); text-transform: uppercase; white-space: nowrap;
  }

  .contact {
    position: absolute; right: 32px; top: 305px;
    text-align: right; color: var(--paper);
  }
  .contact__name {
    font-family: "Cinzel", serif; font-weight: 700;
    font-size: 24px; letter-spacing: 0.08em;
    margin-bottom: 18px;
  }
  .contact__line {
    font-family: "Open Sans", sans-serif; font-size: 19px;
    line-height: 35px;
    display: flex; justify-content: flex-end; align-items: center; gap: 8px;
  }
  .contact__icon { width: 16px; height: 16px; flex: none; }

  .back-mark {
    position: absolute; left: 286px; top: 80px;
    width: 280px; height: 280px;
    border: 3px solid var(--soft-white); border-radius: 50%;
    display: flex; align-items: center; justify-content: center;
  }
  .back-mark__name {
    font-family: "Montserrat", sans-serif; font-size: 22px;
    letter-spacing: 0.12em; color: var(--soft-white);
    text-transform: uppercase; text-align: center; line-height: 1.5;
  }
  .back-url {
    position: absolute; left: 0; right: 0; top: 420px;
    text-align: center;
    font-family: "Montserrat", sans-serif; font-size: 19px;
    letter-spacing: 0.2em; color: var(--soft-white);
    text-transform: uppercase;
  }
</style>
</head>
<body>
<main class="canvas">

  <section class="card card--front">
    <svg class="card__shapes" viewBox="0 0 854 485" aria-hidden="true">
      <path fill="var(--pink)" d="M0,358 C150,420 330,420 470,360 C530,334 575,302 612,268 C560,322 420,398 270,410 C160,418 80,405 0,396 Z"/>
      <path fill="var(--card-dark)" d="M0,405 C120,440 260,455 420,400 C600,330 760,200 854,22 L854,485 L0,485 Z"/>
    </svg>

    <div class="brand-mark">
      <span class="brand-mark__name">Corvid<br>Lens Studio</span>
    </div>

    <h1 class="wordmark">Corvid Lens Studio</h1>

    <div class="contact">
      <p class="contact__name">Tobiah</p>
      <p class="contact__line">
        <svg class="contact__icon" viewBox="0 0 16 16" aria-hidden="true">
          <circle cx="8" cy="8" r="7" fill="none" stroke="currentColor" stroke-width="1.4"/>
          <path d="M5.5,4.5 L7,4.2 L7.6,6.3 L6.6,7 C7,8 7.8,8.9 8.9,9.4 L9.6,8.4 L11.6,9 L11.4,10.6 C8.4,11 5,7.6 5.5,4.5 Z" fill="currentColor"/>
        </svg>
        0417395268
      </p>
      <p class="contact__line">
        <svg class="contact__icon" viewBox="0 0 16 16" aria-hidden="true">
          <g fill="none" stroke="currentColor" stroke-width="1.2">
            <circle cx="8" cy="8" r="6.8"/>
            <ellipse cx="8" cy="8" rx="3" ry="6.8"/>
            <path d="M1.2,8 H14.8 M2.3,4.6 H13.7 M2.3,11.4 H13.7"/>
          </g>
        </svg>
        www.corvidlensstudio.com.au
      </p>
      <p class="contact__line">
        <svg class="contact__icon" viewBox="0 0 16 16" aria-hidden="true">
          <rect x="0" y="0" width="16" height="16" rx="2" fill="#4a67ad"/>
        </svg>
        corvidlensstudio
      </p>
    </div>
  </section>

  <section class="card card--back">
    <div class="back-mark">
      <span class="back-mark__name">Corvid<br>Lens Studio</span>
    </div>
    <p class="back-url">www.corvidlensstudio.com.au</p>
  </section>

</main>
</body>
</html>
```